Stylish Business Card for Modern hair salon

I need a simple business card design using our salon logo and colours that are in the logo. We service clients of all ages but predominantly those in the 18 to 55 age range. We have a young staff and are looking to have a card that will present a modern and clean image that represents who we are. The card should be in black and white same as our logo. Minimal use of other colours is allowed.

Industry/Entity Type

Hair And Beauty

Contact Information for Business Card

The design should have the following information
salon name - TR Hair Studio
address - 2751 Birchfield Rd.E. Mississauga, ON L7P3K2
phone - 905 614-2870
website - trhairexample.ca
instagram - tr.hairstudio
twitter - @TR_HairStudio

Colors
000000
ffffff
474747

Requirements
Must have
• simple design, salon name, address, phone, website, instagram, twitter info
• Back of card should have the following:
• YOUR NEXT APPOINTMENT
• DATE
• TIME
Nice to have
• simple design, clear to see and read,
• predominantly black and white colour, minimal use of other colours is ok
Should not have
• many colours, various fonts

```html
<!DOCTYPE html>
<html lang="en">
<head>
<meta charset="utf-8">
<title>TR Hair Studio – Business Card</title>
<link rel="stylesheet" href="https://fonts.googleapis.com/css2?family=Open+Sans:wdth,wght@75..100,400..700&display=swap">
<style>
  :root {
    --ink: #000000;
    --paper: #ffffff;
    --charcoal: #474747;
    --hair-grey: #b4b4b4;
    --hair-light: #e2e2e2;
  }
  * { box-sizing: border-box; margin: 0; padding: 0; }
  html, body { width: 1200px; height: 414px; overflow: hidden; background: var(--paper); }
  body { font-family: "Open Sans", Arial, sans-serif; color: var(--ink); }

  .card { position: relative; width: 1200px; height: 414px; overflow: hidden; background: var(--paper); }

  /* back side: appointment */
  .back-band { position: absolute; left: 0; top: 0; width: 596px; height: 208px; background: var(--ink); }
  .hair-dark {
    position: absolute; left: 0; top: 208px; width: 240px; height: 170px;
    background: linear-gradient(180deg, var(--ink) 0%, var(--ink) 45%, rgba(0,0,0,0.55) 80%, rgba(0,0,0,0) 100%);
  }
  .back-name {
    position: absolute; left: 290px; top: 118px; width: 300px; text-align: center;
    color: var(--paper); font-weight: 700; font-size: 38px; line-height: 1; letter-spacing: 1px;
  }
  .appointment { position: absolute; left: 244px; top: 250px; width: 340px; }
  .appointment-title {
    font-weight: 700; font-size: 24px; line-height: 1.2; text-decoration: underline; text-decoration-thickness: 2px;
    text-underline-offset: 4px; margin-bottom: 14px;
  }
  .appointment-field {
    display: flex; align-items: flex-end; margin-left: 14px; height: 36px; margin-bottom: 8px;
    font-stretch: 75%; font-size: 22px; color: var(--ink);
  }
  .appointment-field .blank { flex: 1; border-bottom: 1.5px solid var(--ink); margin-left: 4px; margin-bottom: 5px; }

  /* front side: contact */
  .hair-light {
    position: absolute; left: 600px; top: 0; width: 600px; height: 352px;
    background: linear-gradient(180deg, var(--hair-grey) 0%, var(--hair-light) 70%, rgba(255,255,255,0) 100%);
    opacity: 0.85;
  }
  .front-name {
    position: absolute; left: 660px; top: 134px; width: 480px; text-align: center;
    font-weight: 700; font-size: 46px; line-height: 1; letter-spacing: 1px; color: var(--ink);
  }
  .rule-horizontal { position: absolute; left: 598px; top: 265px; width: 602px; height: 2px; background: var(--ink); }
  .rule-vertical { position: absolute; left: 973px; top: 266px; width: 2px; height: 148px; background: var(--ink); }

  .contact-list { position: absolute; left: 644px; top: 278px; list-style: none; }
  .contact-item { display: flex; align-items: center; height: 30px; font-size: 17px; color: var(--charcoal); }
  .contact-item svg { width: 14px; height: 14px; margin-right: 14px; flex: none; }
  .contact-item.address { font-stretch: 75%; font-size: 14px; }

  .social-list { position: absolute; left: 994px; top: 279px; list-style: none; }
  .social-item { display: flex; align-items: center; height: 34px; font-size: 17px; color: var(--charcoal); }
  .social-dot { width: 15px; height: 15px; border-radius: 50%; background: var(--charcoal); margin-right: 8px; flex: none; }
</style>
</head>
<body>
<main class="card">
  <section class="card-back" aria-label="Appointment side">
    <div class="back-band"></div>
    <div class="hair-dark" role="img" aria-label="Black flowing hair illustration"></div>
    <p class="back-name">TR Hair Studio</p>
    <div class="appointment">
      <h2 class="appointment-title">Your next appointment :</h2>
      <p class="appointment-field">Date :<span class="blank"></span></p>
      <p class="appointment-field">Time :<span class="blank"></span></p>
    </div>
  </section>

  <section class="card-front" aria-label="Contact side">
    <div class="hair-light" role="img" aria-label="Light grey flowing hair illustration"></div>
    <p class="front-name">TR Hair Studio</p>
    <div class="rule-horizontal"></div>
    <div class="rule-vertical"></div>

    <ul class="contact-list">
      <li class="contact-item">
        <svg viewBox="0 0 14 14" aria-hidden="true"><rect x="4" y="1" width="6" height="12" rx="1.2" fill="#474747"/><rect x="5" y="2.5" width="4" height="8" fill="#fff"/></svg>
        phone : 905 614-2870
      </li>
      <li class="contact-item address">
        <svg viewBox="0 0 14 14" aria-hidden="true"><rect x="2" y="4" width="10" height="7" fill="#474747"/><path d="M2 4 L7 8 L12 4" stroke="#fff" stroke-width="1" fill="none"/></svg>
        address : 2751 Birchfield Rd.E. Mississauga, ON L7P3K2
      </li>
      <li class="contact-item">
        <svg viewBox="0 0 14 14" aria-hidden="true"><circle cx="7" cy="7" r="5.5" fill="none" stroke="#474747" stroke-width="1.3"/><ellipse cx="7" cy="7" rx="2.4" ry="5.5" fill="none" stroke="#474747" stroke-width="1"/><line x1="1.5" y1="7" x2="12.5" y2="7" stroke="#474747" stroke-width="1"/></svg>
        website : trhairexample.ca
      </li>
    </ul>

    <ul class="social-list">
      <li class="social-item"><span class="social-dot"></span>: @TR_HairStudio</li>
      <li class="social-item"><span class="social-dot"></span>: tr.hairstudio</li>
    </ul>
  </section>
</main>
</body>
</html>
```